Business cards needed

[UPDATE] Source files for logo now uploaded!

Hi there

Looking for a quick turnaround on business cards. I need to be able to have them designed and printed before the weekend.

Each business card will be custom as each person has their own superhero! I've attached the heroes.

The cards need to say:

Bellquist Forge & Crew

Tom Halvik

'Zark' (hero name)

tom@hqz-mail.co

www.hqz-mail.co

Skype tomhalvik

@jq8

I've uploaded the source files for the logo! Thanks!

```html
<!DOCTYPE html>
<html lang="en">
<head>
<meta charset="utf-8">
<title>Bellquist Forge &amp; Crew — Business Card</title>
<link href="https://fonts.googleapis.com/css2?family=Open+Sans:wght@300;400;600&display=swap" rel="stylesheet">
<style>
  :root {
    --brand-red: #e04b58;
    --brand-red-dark: #c93c49;
    --paper: #ffffff;
    --ink: #222222;
    --ink-soft: #6b6b6b;
    --hero-blue: #2d5a9a;
    --hero-light: #cfe3f6;
    --backdrop: #3a3a3a;
  }
  * { box-sizing: border-box; margin: 0; padding: 0; }
  html, body { width: 1200px; height: 800px; overflow: hidden; }
  body {
    background: var(--backdrop);
    font-family: "Open Sans", sans-serif;
    display: flex;
    align-items: center;
    justify-content: center;
    gap: 40px;
  }
  .card {
    width: 540px;
    height: 309px;
    position: relative;
    overflow: hidden;
    box-shadow: 0 8px 24px rgba(0,0,0,.35);
  }

  /* Front */
  .card--front { background: var(--paper); }
  .front__band {
    position: absolute; left: 0; top: 0; bottom: 0;
    width: 58px;
    background: var(--brand-red);
    display: flex; align-items: center; justify-content: center;
  }
  .front__band-mark {
    color: var(--paper);
    font-weight: 600;
    font-size: 11px;
    letter-spacing: .5px;
    white-space: nowrap;
    transform: rotate(-90deg);
  }
  .front__hero {
    position: absolute; left: 58px; top: 0; bottom: 0;
    width: 200px;
    background: linear-gradient(160deg, var(--hero-light) 0%, var(--hero-blue) 55%, #1f3f73 100%);
  }
  .front__details {
    position: absolute; right: 26px; top: 34px;
    width: 250px;
    text-align: right;
  }
  .front__brand {
    display: flex; align-items: center; justify-content: flex-end; gap: 8px;
    color: var(--brand-red);
    font-weight: 600;
    font-size: 19px;
    line-height: 1.1;
  }
  .front__brand-square {
    width: 14px; height: 14px; background: var(--brand-red); flex: none;
  }
  .front__company {
    margin-top: 6px;
    font-size: 11px;
    font-weight: 300;
    color: var(--ink-soft);
  }
  .front__name {
    margin-top: 18px;
    font-size: 24px;
    font-weight: 400;
    color: var(--ink);
    line-height: 1.1;
  }
  .front__hero-name {
    font-size: 15px;
    font-weight: 300;
    color: var(--ink-soft);
  }
  .contact-list {
    list-style: none;
    margin-top: 16px;
  }
  .contact-list__item {
    display: flex; align-items: center; justify-content: flex-end; gap: 6px;
    font-size: 13px;
    font-weight: 300;
    color: var(--ink);
    line-height: 1.55;
  }
  .contact-list__item b { font-weight: 600; }
  .contact-icon {
    width: 12px; height: 12px; flex: none;
  }

  /* Back */
  .card--back {
    background: var(--brand-red);
    display: flex; align-items: center; justify-content: center;
  }
  .back__brand {
    display: flex; align-items: center; gap: 12px;
    color: var(--paper);
    font-weight: 600;
    font-size: 30px;
  }
  .back__brand-square {
    width: 22px; height: 22px; background: var(--paper);
  }
  .back__tagline {
    position: absolute; left: 0; right: 0; top: 190px;
    text-align: center;
    color: var(--paper);
    font-weight: 300;
    font-size: 15px;
  }
</style>
</head>
<body>

  <section class="card card--front" aria-label="Card front">
    <div class="front__band">
      <span class="front__band-mark">Bellquist Forge &amp; Crew</span>
    </div>
    <div class="front__hero" role="img" aria-label="Illustration of the superhero Zark in a blue suit with lightning"></div>

    <div class="front__details">
      <div class="front__brand"><span class="front__brand-square"></span>Bellquist Forge &amp; Crew</div>
      <p class="front__company">Bellquist Forge &amp; Crew</p>
      <h1 class="front__name">Tom Halvik</h1>
      <p class="front__hero-name">Zark</p>
      <ul class="contact-list">
        <li class="contact-list__item">tom@hqz-mail.co
          <svg class="contact-icon" viewBox="0 0 12 12"><rect width="12" height="12" rx="2" fill="#e04b58"/><path d="M2.5 4l3.5 2.5L9.5 4" stroke="#fff" stroke-width="1" fill="none"/></svg>
        </li>
        <li class="contact-list__item">www.<b>hqz-mail</b>.co
          <svg class="contact-icon" viewBox="0 0 12 12"><circle cx="6" cy="6" r="6" fill="#e04b58"/><circle cx="6" cy="6" r="3.5" stroke="#fff" stroke-width=".9" fill="none"/><path d="M2.5 6h7M6 2.5v7" stroke="#fff" stroke-width=".9"/></svg>
        </li>
        <li class="contact-list__item">tomhalvik
          <svg class="contact-icon" viewBox="0 0 12 12"><circle cx="6" cy="6" r="6" fill="#e04b58"/></svg>
        </li>
        <li class="contact-list__item">@jq8
          <svg class="contact-icon" viewBox="0 0 12 12"><circle cx="6" cy="6" r="6" fill="#e04b58"/></svg>
        </li>
      </ul>
    </div>
  </section>

  <section class="card card--back" aria-label="Card back">
    <div class="back__brand"><span class="back__brand-square"></span>Bellquist Forge &amp; Crew</div>
  </section>

</body>
</html>
```